Business Card Design For Financial Company

Create a new design for company's business card. The corporate logo is attached in several formats. Our new website design is also attached and we would like the business cards to reflect this.
Card needs to contain the following info:
Name
Job Title
Legal company name - eg Varomel Holdings (Asia) Ltd
Address - eg 517-09 Brellford Plaza,46 Tamsworth Lane, Hong Kong
Direct tel
Main tel
Fax
Email
Website URL
MS word format preferred. Other formats that can be edited on standard PC also OK.
Updates
Please note the the "VAROMEL" logo nameĀ font is "Gill Sans MT" on Windows
Target Market(s)
Instituation Investors
Industry/Entity Type
Business
Look and feel
Each slider illustrates characteristics of the customer's brand and the style your logo design should communicate.

```html
<!DOCTYPE html>
<html lang="en">
<head>
<meta charset="utf-8">
<title>Varomel Holdings – Business Card</title>
<link rel="stylesheet" href="https://fonts.googleapis.com/css2?family=Cabin:wght@400;500&display=swap">
<style>
  :root {
    --backdrop: #97a1a8;
    --brand-red: #d30f1d;
    --brand-maroon: #740000;
    --card-white: #ffffff;
    --ink: #1a1a1a;
    --card-shadow: rgba(0, 0, 0, 0.85);
  }
  html, body {
    margin: 0;
    padding: 0;
    width: 1200px;
    height: 900px;
    overflow: hidden;
    background: var(--backdrop);
    font-family: "Cabin", "Gill Sans", "Gill Sans MT", sans-serif;
  }
  .canvas {
    position: relative;
    width: 1200px;
    height: 900px;
  }
  .card {
    position: absolute;
    left: 336px;
    width: 607px;
    height: 372px;
    border-radius: 28px;
    overflow: hidden;
    box-shadow: 5px 5px 4px var(--card-shadow);
  }
  .card-front {
    top: 60px;
    background: var(--brand-red);
  }
  .front-emblem {
    position: absolute;
    left: 373px;
    top: 139px;
    width: 192px;
    height: 192px;
    border-radius: 50%;
    background: var(--brand-maroon);
  }
  .card-back {
    top: 460px;
    height: 371px;
    background: var(--card-white);
  }
  .brand-panel {
    position: absolute;
    left: 0;
    top: 0;
    width: 217px;
    height: 100%;
    background: var(--brand-red);
  }
  .brand-dot {
    position: absolute;
    left: 80px;
    top: 132px;
    width: 60px;
    height: 60px;
    border-radius: 50%;
    background: var(--brand-maroon);
  }
  .brand-name {
    position: absolute;
    left: 0;
    width: 217px;
    top: 199px;
    text-align: center;
    color: var(--card-white);
    font-size: 27px;
    font-weight: 400;
    letter-spacing: 0.5px;
    line-height: 1;
  }
  .details {
    position: absolute;
    left: 276px;
    top: 34px;
    color: var(--ink);
    font-size: 19px;
    line-height: 25.7px;
  }
  .details p { margin: 0; }
  .person-name { font-weight: 500; }
  .company-block { margin-top: 11px !important; }
  .contact-block { margin-top: 11px !important; }
</style>
</head>
<body>
<main class="canvas">
  <section class="card card-front" aria-label="Business card front">
    <div class="front-emblem"></div>
  </section>

  <section class="card card-back" aria-label="Business card back">
    <div class="brand-panel">
      <div class="brand-dot"></div>
      <div class="brand-name">VAROMEL</div>
    </div>
    <div class="details">
      <p class="person-name">Daniel Mercer</p>
      <p class="job-title">Sales Manager</p>
      <p class="company-block">Varomel Holdings (Asia) Ltd<br>
        517-09 Brellford Plaza<br>
        46 Tamsworth Lane<br>
        Hong Kong</p>
      <p class="contact-block">main tel: 318 602 4475<br>
        direct tel: 447 219 6083<br>
        fax: 021 354 7698<br>
        e-mail: contact@varomelholdings.com<br>
        url: www.varomelholdings.com</p>
    </div>
  </section>
</main>
</body>
</html>
```